Borvella Gelato Pints

6 flavors , pints italian , southern , organic , natural feel

Pistachio , chocolate, strawberry , hazelnut , vaniglia

Stracciiatelle

Target Market(s)

Upscale

Requirements
Must have
• See graphic upload . Want that look.. showing freshbest quality in gradients of each flavor

```html
<!DOCTYPE html>
<html lang="en">
<head>
<meta charset="utf-8">
<title>Borvella Gelato Pints</title>
<link rel="stylesheet" href="https://fonts.googleapis.com/css2?family=Barlow+Condensed:wght@400&family=Barlow+Semi+Condensed:wght@500&display=swap">
<style>
  :root {
    --page: #ffffff;
    --cream: #f7f3ea;
    --brown: #4a2617;
    --brown-ink: #5a3322;
    --pistachio: #d6e5bf;
    --chocolate: #e2dcd1;
    --strawberry: #f2c5cb;
    --hazelnut: #f3e1d2;
    --vaniglia: #f4eca3;
    --stracciatella: #ffffff;
  }
  * { box-sizing: border-box; margin: 0; padding: 0; }
  html, body { width: 1200px; height: 1166px; overflow: hidden; background: var(--page); }
  .sheet { position: relative; width: 1200px; height: 1166px; }

  .seal {
    position: absolute; top: 52px; width: 278px; height: 278px;
    border-radius: 50%; background: var(--cream);
    display: flex; align-items: center; justify-content: center;
  }
  .seal::after {
    content: ""; position: absolute; inset: 13px;
    border: 1px solid var(--brown-ink); border-radius: 50%;
  }
  .seal .brand-name { font-size: 34px; }

  .brand-name {
    font-family: "Barlow Condensed", sans-serif; font-weight: 400;
    color: var(--brown-ink); letter-spacing: 0.02em; white-space: nowrap;
  }

  .pint-label {
    position: absolute; width: 268px; height: 300px; background: var(--cream);
  }
  .pint-label .brand-name {
    position: absolute; top: 52px; left: 0; right: 0; text-align: center; font-size: 27px;
  }
  .flavor-art {
    position: absolute; top: 100px; left: 59px; width: 150px; height: 118px;
    border-radius: 50%;
  }
  .flavor-name {
    position: absolute; top: 233px; left: 67px; width: 136px; height: 20px;
    border-radius: 4px 10px 6px 12px;
    font-family: "Barlow Semi Condensed", sans-serif; font-weight: 500;
    font-size: 12.5px; letter-spacing: 0.1em; color: var(--brown-ink);
    display: flex; align-items: center; justify-content: center;
  }
  .volume {
    position: absolute; top: 273px; left: 112px; width: 44px; height: 27px;
    background: var(--brown); color: var(--cream);
    font-family: "Barlow Semi Condensed", sans-serif; font-weight: 500; font-size: 9.5px;
    display: flex; align-items: center; justify-content: center; letter-spacing: 0.04em;
  }

  .pistachio .flavor-art { background: radial-gradient(ellipse at 50% 55%, #b9d27f 0%, #e6c199 45%, rgba(247,243,234,0) 72%); }
  .pistachio .flavor-name { background: var(--pistachio); }
  .chocolate .flavor-art { background: radial-gradient(ellipse at 50% 55%, #3c1a12 0%, #5b2b1c 40%, rgba(247,243,234,0) 72%); }
  .chocolate .flavor-name { background: var(--chocolate); }
  .strawberry .flavor-art { background: radial-gradient(ellipse at 50% 55%, #d8202a 0%, #e5454a 42%, rgba(247,243,234,0) 72%); }
  .strawberry .flavor-name { background: var(--strawberry); }
  .hazelnut .flavor-art { background: radial-gradient(ellipse at 50% 55%, #8a4a24 0%, #b0733f 42%, rgba(247,243,234,0) 72%); }
  .hazelnut .flavor-name { background: var(--hazelnut); }
  .vaniglia .flavor-art { background: radial-gradient(ellipse at 50% 55%, #f2e04a 0%, #e8d36a 30%, #5a3322 48%, rgba(247,243,234,0) 72%); }
  .vaniglia .flavor-name { background: var(--vaniglia); }
  .stracciatella .flavor-art { background: radial-gradient(ellipse at 50% 55%, #ffffff 0%, #eeebe4 45%, rgba(247,243,234,0) 72%); }
  .stracciatella .flavor-name { background: var(--stracciatella); }
</style>
</head>
<body>
<main class="sheet">
  <div class="seal" style="left:84px"><span class="brand-name">Borvella Gelato</span></div>
  <div class="seal" style="left:452px"><span class="brand-name">Borvella Gelato</span></div>
  <div class="seal" style="left:820px"><span class="brand-name">Borvella Gelato</span></div>

  <section class="pint-label pistachio" style="left:87px;top:361px">
    <span class="brand-name">Borvella Gelato</span>
    <div class="flavor-art" role="img" aria-label="Watercolour illustration of pistachio nuts"></div>
    <p class="flavor-name">PISTACHIO</p>
    <p class="volume">473ML</p>
  </section>
  <section class="pint-label chocolate" style="left:455px;top:361px">
    <span class="brand-name">Borvella Gelato</span>
    <div class="flavor-art" role="img" aria-label="Watercolour illustration of chocolate pieces and cocoa beans"></div>
    <p class="flavor-name">CHOCOLATE</p>
    <p class="volume">473ML</p>
  </section>
  <section class="pint-label strawberry" style="left:822px;top:361px">
    <span class="brand-name">Borvella Gelato</span>
    <div class="flavor-art" role="img" aria-label="Watercolour illustration of two strawberries"></div>
    <p class="flavor-name">STRAWBERRY</p>
    <p class="volume">473ML</p>
  </section>

  <section class="pint-label hazelnut" style="left:86px;top:702px">
    <span class="brand-name">Borvella Gelato</span>
    <div class="flavor-art" role="img" aria-label="Watercolour illustration of hazelnuts with a leaf"></div>
    <p class="flavor-name">HAZELNUT</p>
    <p class="volume">473ML</p>
  </section>
  <section class="pint-label vaniglia" style="left:454px;top:702px">
    <span class="brand-name">Borvella Gelato</span>
    <div class="flavor-art" role="img" aria-label="Watercolour illustration of a vanilla flower and pods"></div>
    <p class="flavor-name">VANIGLIA</p>
    <p class="volume">473ML</p>
  </section>
  <section class="pint-label stracciatella" style="left:821px;top:702px">
    <span class="brand-name">Borvella Gelato</span>
    <div class="flavor-art" role="img" aria-label="Watercolour illustration of a round of fresh white cheese"></div>
    <p class="flavor-name">STRACCIATELLA</p>
    <p class="volume">473ML</p>
  </section>
</main>
</body>
</html>
```